Business Card Design

Take existing logo/brand and develop business card for sales team.
We have two separate brands and require a business card for each.

1. VoxHarbor
2. MyNimbusLinko

Refer to our websites www.voxharbor.example.au and www.mynimbuslinko.example.au for designs currently implemented and in the marketplace.

Both cards are brands of our parent company Quorra Systems Pty Ltd - an Australian Telecommunications company in the medium business sector. We have only business customers, no retail/residential consumers.

Target Market(s)

Australian Business - small to medium enterprise

Industry/Entity Type

Business

Contact Information for Business Card

Lev Dorrit
Sales Director
Mobile: +61 400 555 187
Direct: +61 3 9555 0137
Email: lev@voxharbor.example.au
VoxHarbor (a brand of Quorra Systems Pty Ltd)

Lev Dorrit
Sales Director
Mobile: +61 400 555 187
Direct: +61 3 9555 0137
Email: lev@mynimbuslinko.example.au
MyNimbusLinko (a brand of Quorra Systems Pty Ltd)

Font styles to use
Sans Serif
Other font styles liked:
• Roboto Condensed, Open Sans

Requirements
Must have
• Clean lines, crisp fonts - suggest Roboto Condensed or similar.
• Must be easy to read and clear.
• Brand colour #0C8CCD
• Two colour maximum
Nice to have
• Modern, intellectual and unique design.
Should not have
• No die cuts
• No copies or rip-offs of other designs

```html
<!DOCTYPE html>
<html lang="en">
<head>
<meta charset="utf-8">
<title>VoxHarbor Business Card</title>
<link rel="stylesheet" href="https://fonts.googleapis.com/css2?family=Roboto:wght@400;500;700&display=swap">
<style>
  :root {
    --brand: #0C8CCD;
    --ink: #3a3a3a;
    --paper: #ffffff;
    --paper-shade: #f1f2f3;
    --backdrop: #2a2a2a;
  }
  * { margin: 0; padding: 0; box-sizing: border-box; }
  html, body { width: 1200px; height: 900px; overflow: hidden; }
  body {
    background: var(--backdrop);
    font-family: "Roboto", Arial, sans-serif;
    position: relative;
  }
  .card {
    position: absolute;
    left: 240px;
    width: 720px;
    height: 400px;
    overflow: hidden;
    box-shadow: 0 10px 30px rgba(0,0,0,.5);
  }
  /* Front */
  .card--front { top: 40px; background: var(--brand); }
  .front-ring { position: absolute; inset: 0; }
  .front-brand {
    position: absolute;
    left: 300px; top: 160px;
    transform: translateX(-50%);
    display: flex; align-items: center; gap: 16px;
    color: var(--brand);
    font-size: 58px; font-weight: 400;
    letter-spacing: 1px;
  }
  .brand-dot {
    width: 48px; height: 48px; border-radius: 50%;
    background: var(--brand);
  }
  .front-url {
    position: absolute;
    left: 300px; top: 300px;
    transform: translateX(-50%);
    color: var(--brand);
    font-size: 16px;
    letter-spacing: .5px;
  }
  /* Back */
  .card--back {
    top: 460px;
    background: linear-gradient(160deg, var(--paper) 40%, var(--paper-shade));
  }
  .back-brand {
    position: absolute;
    right: 50px; top: 48px;
    display: flex; align-items: center; gap: 12px;
    color: var(--brand);
    font-size: 44px; font-weight: 400;
  }
  .back-brand .brand-dot { width: 52px; height: 52px; }
  .contact {
    position: absolute;
    left: 56px; bottom: 52px;
    color: var(--ink);
  }
  .contact__name { color: var(--brand); font-weight: 700; font-size: 20px; }
  .contact__title { font-size: 19px; margin-bottom: 18px; }
  .contact__list { display: grid; grid-template-columns: 78px auto; row-gap: 4px; font-size: 20px; }
  .contact__label { color: var(--brand); font-weight: 500; }
  .parent {
    position: absolute;
    right: 70px; top: 222px;
    text-align: right;
    color: var(--brand);
    font-size: 14px;
    line-height: 1.35;
  }
  .parent strong { font-weight: 700; }
  .edge-square {
    position: absolute;
    right: 0; top: 200px;
    width: 46px; height: 46px;
    background: var(--brand);
  }
</style>
</head>
<body>
  <section class="card card--front">
    <svg class="front-ring" width="720" height="400" viewBox="0 0 720 400" aria-hidden="true">
      <circle cx="300" cy="200" r="235" fill="#ffffff"/>
    </svg>
    <div class="front-brand"><span class="brand-dot"></span>VoxHarbor</div>
    <div class="front-url">www.voxharbor.example.au</div>
  </section>

  <section class="card card--back">
    <div class="back-brand"><span class="brand-dot"></span>VoxHarbor</div>

    <div class="parent"><strong>VoxHarbor</strong> a brand of<br>Quorra Systems Pty Ltd</div>
    <div class="edge-square"></div>

    <div class="contact">
      <div class="contact__name">Lev Dorrit</div>
      <div class="contact__title">Sales Director</div>
      <div class="contact__list">
        <span class="contact__label">Mobile:</span><span>+61 400 555 187</span>
        <span class="contact__label">Direct:</span><span>+61 3 9555 0137</span>
        <span class="contact__label">Email:</span><span>lev@voxharbor.example.au</span>
      </div>
    </div>
  </section>
</body>
</html>
```